New eyelid plastic surgery office needs a business card design-Eyelid Specialists of the Brenwick

I recently used DraftHarbor for my logo design and was very pleased with creativity and results. It was a difficult decision for me. Now I would like to create a business card based on this logo, which I will attach.

The text should be easily legible as some of my patients have difficulty seeing, but I would like a subtle, sophisticated artistry also evident to make the card memorable. Would like the card based on a similar color scheme as the logo but the inverse or other complementary colors may prove interesting

A good question was asked...my concern about my visually impaired patients was really my desire to avoid italicized or calligraphic type fonts that may be hard to read. Standard font size for a business card would be fine. Thanks!

Thank you so much for the great work so far. I wanted to give you my particular contact information to see if that would change the look of the cards. Martin Holloway, MD Address: 2871 Larkspur Lane, Suite 215 Wilmington, NC 39512 Phone: 555-382-1946 Fax: 555-382-1947 Website: www.brenwickliddesign.example Please delete the email slot from the card. Thanks so much!

Reason: Last minute consideration. So many great revisions right now!

Plastic

```html
<!DOCTYPE html>
<html lang="en">
<head>
<meta charset="utf-8">
<title>Eyelid Specialists of the Brenwick – Business Card</title>
<link rel="stylesheet" href="https://fonts.googleapis.com/css2?family=Exo+2:wght@400;500;600&display=swap">
<style>
  :root {
    --page-bg: #e9e6e2;
    --card-bg: #ffffff;
    --card-shade: #eceef0;
    --brand-blue: #2a6db8;
    --band-deep: #2b3fae;
    --band-bright: #14a6e6;
    --swoosh-grey: #6b6f75;
    --ink: #2a2d33;
    --white: #ffffff;
  }
  * { box-sizing: border-box; margin: 0; padding: 0; }
  html, body {
    width: 1200px; height: 900px; overflow: hidden;
    background: var(--page-bg);
    font-family: "Exo 2", sans-serif;
  }
  .sheet {
    width: 1200px; height: 900px;
    display: flex; flex-direction: column;
    align-items: center; justify-content: center; gap: 44px;
  }
  .card {
    position: relative;
    width: 620px; height: 354px;
    background: radial-gradient(ellipse at 50% 40%, var(--card-bg) 45%, var(--card-shade) 100%);
    box-shadow: 0 6px 18px rgba(0,0,0,.18);
    overflow: hidden;
  }
  .brand-name {
    color: var(--brand-blue);
    font-weight: 500;
    text-transform: uppercase;
    line-height: 1.05;
  }
  .card-front .brand-name {
    position: absolute; left: 38px; top: 44px;
    font-size: 27px; letter-spacing: 1px;
  }
  .card-front .brand-name .brand-line-sub { font-size: 15px; letter-spacing: 1.6px; display: block; margin-top: 4px; }
  .contact {
    position: absolute; left: 372px; top: 40px;
    color: var(--ink); list-style: none;
    font-size: 13px; letter-spacing: .4px;
  }
  .contact .address { font-size: 15px; font-weight: 500; line-height: 1.35; margin-bottom: 16px; letter-spacing: .6px; }
  .contact li { display: flex; align-items: center; gap: 8px; margin-bottom: 7px; }
  .contact svg { width: 13px; height: 13px; flex: none; fill: var(--brand-blue); }
  .band { position: absolute; left: 0; top: 0; width: 620px; height: 354px; }
  .holder {
    position: absolute; left: 40px; top: 262px; color: var(--white);
  }
  .holder-name { font-size: 21px; font-weight: 500; letter-spacing: 1.5px; text-transform: uppercase; }
  .holder-role { font-size: 14px; margin-top: 3px; letter-spacing: .5px; }
  .card-back { display: flex; align-items: center; justify-content: center; }
  .card-back .brand-name { text-align: center; font-size: 33px; letter-spacing: 1.5px; }
  .card-back .brand-name .brand-line-sub { display: block; font-size: 17px; letter-spacing: 2px; margin-top: 6px; }
</style>
</head>
<body>
<main class="sheet">
  <section class="card card-front" aria-label="Card front">
    <svg class="band" viewBox="0 0 620 354" aria-hidden="true">
      <defs>
        <linearGradient id="bandFill" x1="0" y1="0" x2="1" y2="0">
          <stop offset="0" stop-color="var(--band-deep)"/>
          <stop offset=".55" stop-color="var(--band-bright)"/>
          <stop offset="1" stop-color="var(--band-deep)"/>
        </linearGradient>
      </defs>
      <path d="M0 222 C120 196 210 250 330 262 C430 272 520 250 620 292 L620 354 L0 354 Z" fill="var(--swoosh-grey)" opacity=".55"/>
      <path d="M0 214 C120 186 210 236 330 250 C440 262 530 244 620 286 L620 354 L0 354 Z" fill="url(#bandFill)"/>
      <path d="M330 250 C440 262 530 244 620 286 L620 296 C525 258 440 274 330 262 Z" fill="var(--white)" opacity=".7"/>
    </svg>
    <div class="brand-name">Eyelid Specialists<span class="brand-line-sub">of the Brenwick</span></div>
    <ul class="contact">
      <li class="address">412 9th Floor Arcade<br>Kestrel Road BRW</li>
      <li><svg viewBox="0 0 16 16"><path d="M3 1l3 3-2 2c1 2 3 4 5 5l2-2 3 3-2 3C7 15 1 9 1 3z"/></svg>555 018 2741</li>
      <li><svg viewBox="0 0 16 16"><path d="M4 1h6l2 2v4h2v8H2V7h2zM5 2v5h6V4H9V2zM4 10h2v2H4zm4 0h4v1H8z"/></svg>555 018 2741</li>
      <li><svg viewBox="0 0 16 16"><path d="M1 3h14v10H1zm1 1v1l6 4 6-4V4z"/></svg>yourname@mailbox.example</li>
      <li><svg viewBox="0 0 16 16"><path d="M8 1a7 7 0 110 14A7 7 0 018 1zm-1 1.6A5.5 5.5 0 002.6 7H5c.2-1.7.9-3.3 2-4.4zM9 2.6c1.1 1.1 1.8 2.7 2 4.4h2.4A5.5 5.5 0 009 2.6zM6 7h4c-.2-1.7-.9-3-2-4-1.1 1-1.8 2.3-2 4zm-3.4 2A5.5 5.5 0 007 13.4C5.9 12.3 5.2 10.7 5 9zm3.4 0c.2 1.7.9 3 2 4 1.1-1 1.8-2.3 2-4zm5 0c-.2 1.7-.9 3.3-2 4.4A5.5 5.5 0 0013.4 9z"/></svg>www.yoursitename.example</li>
    </ul>
    <div class="holder">
      <div class="holder-name">Owen Hartley</div>
      <div class="holder-role">Managing Director</div>
    </div>
  </section>

  <section class="card card-back" aria-label="Card back">
    <div class="brand-name">Eyelid Specialists<span class="brand-line-sub">of the Brenwick</span></div>
  </section>
</main>
</body>
</html>
```